Redo my diagrams for print in a Magazine - files attached - ASAP

Hi, I have 3 diagrams that I have done that are dodgy, that I need to look good. They need to be high quality to be printed in a magazine for an article I am writing. And of course I need them yesterday. Actually I need them in 8 hours.

If there was a A4 version that could be downloaded, that would be excellent.

Cheers

Rob

Target Market(s)

Medial Magazine article

Industry/Entity Type

Medical

Font styles to use
Sans Serif

Requirements
Must have
• Must be able to be printed, in a magazine.
Nice to have
• Nice to have an A4 downloadable version

```html
<!DOCTYPE html>
<html lang="en">
<head>
<meta charset="utf-8">
<title>What People With No Pain Have on Their MRIs</title>
<link rel="stylesheet" href="https://fonts.googleapis.com/css2?family=Raleway:wght@300;400;500;600;700;800&display=swap">
<style>
  :root {
    --paper: #ffffff;
    --ink: #1b1b1b;
    --ink-soft: #444444;
    --rule: #111111;
    --back-red: #e11b35;
    --back-wine: #7a1c2e;
    --knee-lime: #b5d334;
  }
  html, body { margin: 0; padding: 0; overflow: hidden; background: var(--paper); }
  .canvas {
    position: relative; width: 1200px; height: 2553px; overflow: hidden;
    background: var(--paper); color: var(--ink);
    font-family: "Raleway", Arial, sans-serif;
  }
  .panel { position: absolute; left: 0; width: 1200px; }
  .panel--hip { top: 0; height: 849px; border-bottom: 3px solid var(--rule); }
  .panel--back { top: 852px; height: 846px; border-bottom: 3px solid var(--rule); }
  .panel--knee { top: 1701px; height: 852px; }
  .panel-art { position: absolute; left: 0; top: 0; }

  .panel-title {
    position: absolute; left: 0; width: 1200px; margin: 0;
    text-align: center; font-weight: 300; font-size: 44px; line-height: 54px;
    letter-spacing: -0.3px;
  }

  .stat { position: absolute; }
  .stat-value { display: block; font-weight: 800; font-size: 36px; line-height: 1; margin-bottom: 4px; }
  .stat-row { display: flex; align-items: flex-start; }
  .stat-label { font-weight: 500; font-size: 16px; line-height: 20px; white-space: nowrap; }
  .leader { flex: 1; height: 0; border-top: 1.5px solid var(--rule); margin-top: 10px; }
  .stat--left { left: 117px; }
  .stat--left .leader { margin-left: 10px; }
  .stat--right { right: 120px; text-align: right; }
  .stat--right .leader { margin-right: 10px; }
  .stat-row--inline { align-items: center; }
  .stat-row--inline .leader { margin-top: 0; }
  .stat-row--inline .stat-value { display: inline; margin: 0 0 0 8px; }

  .no-pain { position: absolute; margin: 0; }
  .no-pain-value { display: block; font-weight: 800; font-size: 30px; line-height: 36px; }
  .no-pain-note { display: block; font-weight: 500; font-size: 20px; line-height: 26px; }
  .no-pain-note--underlined { text-decoration: underline; text-underline-offset: 4px; }

  .citation {
    position: absolute; margin: 0; font-size: 12px; line-height: 17px; color: var(--ink-soft);
  }
  .citation--centered { left: 150px; width: 900px; text-align: center; }
  .citation--listed { left: 154px; width: 960px; font-size: 11px; line-height: 14px; }

  .age-question {
    position: absolute; right: 780px; top: 610px; margin: 0;
    text-align: right; font-weight: 700; font-size: 19px; line-height: 23px; white-space: nowrap;
  }
  .age-pointer {
    position: absolute; left: 351px; top: 726px; width: 100px; height: 0;
    border-top: 1.5px solid var(--rule);
  }
  .age-pointer::before {
    content: ""; position: absolute; left: -5px; top: -6px; width: 10px; height: 10px;
    border-radius: 50%; background: var(--rule);
  }

  .age-table { position: absolute; left: 451px; top: 614px; width: 329px; height: 140px; display: flex; }
  .age-band {
    width: 17px; color: #fff; font-weight: 800; font-size: 11px; letter-spacing: 0.5px;
    writing-mode: vertical-rl; text-align: center; line-height: 17px;
  }
  .age-band--young { background: var(--back-red); transform: rotate(180deg); }
  .age-band--old { background: var(--back-wine); }
  .age-rows { flex: 1; display: flex; flex-direction: column; justify-content: space-between; padding: 1px 0; }
  .age-row {
    display: grid; grid-template-columns: 34px 18px 1fr 20px 34px; align-items: center;
    font-size: 10.5px; line-height: 16px;
  }
  .age-young { color: var(--back-red); font-weight: 700; text-align: right; padding-right: 3px; }
  .age-old { color: var(--back-wine); font-weight: 700; padding-left: 3px; }
  .age-finding { text-align: center; font-weight: 500; white-space: nowrap; }
  .age-dot { position: relative; height: 0; border-top: 1px solid var(--rule); }
  .age-dot::before {
    content: ""; position: absolute; left: 0; top: -3px; width: 5px; height: 5px; border-radius: 50%; background: var(--rule);
  }
  .age-arrow { position: relative; height: 0; border-top: 1px solid var(--rule); }
  .age-arrow::after {
    content: ""; position: absolute; right: -1px; top: -4px;
    border-left: 6px solid var(--rule); border-top: 3.5px solid transparent; border-bottom: 3.5px solid transparent;
  }

  .meniscus-note {
    position: absolute; left: 864px; top: 599px; width: 222px; margin: 0;
    font-size: 12px; line-height: 17px; font-weight: 500;
  }
  .meniscus-note b { font-weight: 800; }
</style>
</head>
<body>
<main class="canvas">

  <!-- Hip -->
  <section class="panel panel--hip">
    <svg class="panel-art" width="1200" height="849" viewBox="0 0 1200 849">
      <defs>
        <radialGradient id="hip-scan" cx="50%" cy="45%" r="60%">
          <stop offset="0" stop-color="#9c9c9c"/>
          <stop offset="0.6" stop-color="#5c5c5c"/>
          <stop offset="1" stop-color="#262626"/>
        </radialGradient>
      </defs>
      <circle cx="597" cy="424" r="212" fill="url(#hip-scan)" role="img" aria-label="Coronal MRI scan of a hip joint"/>
      <g fill="none" stroke-width="26">
        <circle cx="597" cy="424" r="238" stroke="#161616" stroke-dasharray="75.8 2000" transform="rotate(97 597 424)"/>
        <circle cx="597" cy="424" r="238" stroke="#1b2747" stroke-dasharray="146.4 2000" transform="rotate(115 597 424)"/>
        <circle cx="597" cy="424" r="238" stroke="#223766" stroke-dasharray="146.4 2000" transform="rotate(150 597 424)"/>
        <circle cx="597" cy="424" r="238" stroke="#294c8a" stroke-dasharray="146.4 2000" transform="rotate(185 597 424)"/>
        <circle cx="597" cy="424" r="238" stroke="#2e63aa" stroke-dasharray="146.4 2000" transform="rotate(220 597 424)"/>
        <circle cx="597" cy="424" r="238" stroke="#1c7fc3" stroke-dasharray="146.4 2000" transform="rotate(255 597 424)"/>
        <circle cx="597" cy="424" r="238" stroke="#5c92d0" stroke-dasharray="125.6 2000" transform="rotate(290 597 424)"/>
        <circle cx="597" cy="424" r="238" stroke="#86acda" stroke-dasharray="104.9 2000" transform="rotate(320 597 424)"/>
        <circle cx="597" cy="424" r="238" stroke="#a8c4e5" stroke-dasharray="113.2 2000" transform="rotate(345 597 424)"/>
        <circle cx="597" cy="424" r="238" stroke="#d2deef" stroke-dasharray="124.6 2000" transform="rotate(372 597 424)"/>
      </g>
    </svg>

    <h2 class="panel-title" style="top:24px">What People With No Pain,<br>Have on Their Hip MRI’s</h2>

    <div class="stat stat--left" style="top:198px;width:301px">
      <strong class="stat-value">73%</strong>
      <div class="stat-row"><span class="stat-label">have some sort of abnormality</span><span class="leader"></span></div>
    </div>
    <div class="stat stat--left" style="top:282px;width:246px">
      <strong class="stat-value">69%</strong>
      <div class="stat-row"><span class="stat-label">have labral tears</span><span class="leader"></span></div>
    </div>
    <div class="stat stat--left" style="top:366px;width:229px">
      <strong class="stat-value">24%</strong>
      <div class="stat-row"><span class="stat-label">have cartilage defects</span><span class="leader"></span></div>
    </div>
    <div class="stat stat--left" style="top:451px;width:241px">
      <strong class="stat-value">11%</strong>
      <div class="stat-row"><span class="stat-label">Bone marrow oedema</span><span class="leader"></span></div>
    </div>
    <div class="stat stat--left" style="top:623px;width:448px">
      <strong class="stat-value">2.2%</strong>
      <div class="stat-row"><span class="stat-label">Ligamentum teres tears</span><span class="leader"></span></div>
    </div>

    <div class="stat stat--right" style="top:225px;left:771px">
      <div class="stat-row stat-row--inline"><span class="leader"></span><span class="stat-label">CAM lesions are seens in</span><strong class="stat-value">20%</strong></div>
    </div>
    <div class="stat stat--right" style="top:302px;left:837px">
      <strong class="stat-value">13%</strong>
      <div class="stat-row"><span class="leader"></span><span class="stat-label">Labral and parabral cysts</span></div>
    </div>
    <div class="stat stat--right" style="top:409px;left:845px">
      <strong class="stat-value">16%</strong>
      <div class="stat-row"><span class="leader"></span><span class="stat-label">have subchondral cysts</span></div>
    </div>
    <div class="stat stat--right" style="top:516px;left:804px">
      <strong class="stat-value">11%</strong>
      <div class="stat-row"><span class="leader"></span><span class="stat-label">have rim fracture</span></div>
    </div>

    <p class="no-pain" style="left:792px;top:636px">
      <span class="no-pain-value">0% have pain</span>
      <span class="no-pain-note">Just because its on the scan</span>
      <span class="no-pain-note no-pain-note--underlined">doesn't mean it hurts</span>
    </p>

    <p class="citation citation--centered" style="top:778px">Marlow B, Hadley AT, Lin CP, Fairbrook CD, Orsen A, Castell MJ. Prevalence of abnormal hip findings in asymptomatic participants : a prospective,<br>blinded study. Am J Joint Med. 2012 Dec;40(12):2720-4.</p>
  </section>

  <!-- Back -->
  <section class="panel panel--back">
    <svg class="panel-art" width="1200" height="846" viewBox="0 0 1200 846">
      <defs>
        <radialGradient id="back-scan" cx="55%" cy="45%" r="60%">
          <stop offset="0" stop-color="#8a8a8a"/>
          <stop offset="0.55" stop-color="#4a4a4a"/>
          <stop offset="1" stop-color="#1c1c1c"/>
        </radialGradient>
      </defs>
      <circle cx="620" cy="396" r="204" fill="url(#back-scan)" role="img" aria-label="Sagittal MRI scan of the lumbar spine"/>
      <g fill="none" stroke-width="24">
        <circle cx="620" cy="396" r="228" stroke="#2a1719" stroke-dasharray="80.6 2000" transform="rotate(150 620 396)"/>
        <circle cx="620" cy="396" r="228" stroke="#4b1b25" stroke-dasharray="120.3 2000" transform="rotate(170 620 396)"/>
        <circle cx="620" cy="396" r="228" stroke="#7b1c2f" stroke-dasharray="140.3 2000" transform="rotate(200 620 396)"/>
        <circle cx="620" cy="396" r="228" stroke="#b21a31" stroke-dasharray="120.3 2000" transform="rotate(235 620 396)"/>
        <circle cx="620" cy="396" r="228" stroke="#e11b35" stroke-dasharray="140.3 2000" transform="rotate(265 620 396)"/>
        <circle cx="620" cy="396" r="228" stroke="#c81c33" stroke-dasharray="120.3 2000" transform="rotate(300 620 396)"/>
        <circle cx="620" cy="396" r="228" stroke="#df2f40" stroke-dasharray="100.5 2000" transform="rotate(330 620 396)"/>
        <circle cx="620" cy="396" r="228" stroke="#ea5b5f" stroke-dasharray="100.5 2000" transform="rotate(355 620 396)"/>
        <circle cx="620" cy="396" r="228" stroke="#f08b86" stroke-dasharray="80.6 2000" transform="rotate(380 620 396)"/>
        <circle cx="620" cy="396" r="228" stroke="#f6b6ae" stroke-dasharray="51.7 2000" transform="rotate(400 620 396)"/>
      </g>
    </svg>

    <h2 class="panel-title" style="top:30px">What People With No Pain,<br>Have on Their Back MRI’s</h2>

    <div class="stat stat--left" style="top:222px;width:283px">
      <strong class="stat-value">83%</strong>
      <div class="stat-row"><span class="stat-label">have a disc bulge, protrusion<br>or extrusion (1)</span><span class="leader"></span></div>
    </div>
    <div class="stat stat--left" style="top:322px;width:262px">
      <strong class="stat-value">37%</strong>
      <div class="stat-row"><span class="stat-label">have facet joint arthritis (3)</span><span class="leader"></span></div>
    </div>
    <div class="stat stat--left" style="top:426px;width:278px">
      <strong class="stat-value">33%</strong>
      <div class="stat-row"><span class="stat-label">have high intensity zones (1)</span><span class="leader"></span></div>
    </div>

    <div class="stat stat--right" style="top:222px;left:832px">
      <strong class="stat-value">22%</strong>
      <div class="stat-row"><span class="leader"></span><span class="stat-label">have discs contracting nerves (1)</span></div>
    </div>
    <div class="stat stat--right" style="top:322px;left:862px">
      <strong class="stat-value">23%</strong>
      <div class="stat-row"><span class="leader"></span><span class="stat-label">have annular fissures (3)</span></div>
    </div>
    <div class="stat stat--right" style="top:426px;left:845px">
      <strong class="stat-value">73%</strong>
      <div class="stat-row"><span class="leader"></span><span class="stat-label">Disc degeneration (1)(2)(3)</span></div>
    </div>
    <div class="stat stat--right" style="top:514px;left:790px">
      <strong class="stat-value">17%</strong>
      <div class="stat-row"><span class="leader"></span><span class="stat-label">Disc pushing on Thecal sac (1)</span></div>
    </div>

    <p class="age-question">What's the<br>difference between<br>20 and 80 year olds<br>no back pain? (4)</p>
    <span class="age-pointer"></span>

    <div class="age-table">
      <div class="age-band age-band--young">20 YEAR OLDS</div>
      <div class="age-rows">
        <div class="age-row"><span class="age-young">37%</span><span class="age-dot"></span><span class="age-finding">Disc degeneration</span><span class="age-arrow"></span><span class="age-old">96%</span></div>
        <div class="age-row"><span class="age-young">17%</span><span class="age-dot"></span><span class="age-finding">Disc Signal loss</span><span class="age-arrow"></span><span class="age-old">97%</span></div>
        <div class="age-row"><span class="age-young">24%</span><span class="age-dot"></span><span class="age-finding">Disc height loss</span><span class="age-arrow"></span><span class="age-old">84%</span></div>
        <div class="age-row"><span class="age-young">30%</span><span class="age-dot"></span><span class="age-finding">Disc Bulge</span><span class="age-arrow"></span><span class="age-old">84%</span></div>
        <div class="age-row"><span class="age-young">29%</span><span class="age-dot"></span><span class="age-finding">Disc Protrusion</span><span class="age-arrow"></span><span class="age-old">43%</span></div>
        <div class="age-row"><span class="age-young">19%</span><span class="age-dot"></span><span class="age-finding">Annular fissure</span><span class="age-arrow"></span><span class="age-old">29%</span></div>
        <div class="age-row"><span class="age-young">4%</span><span class="age-dot"></span><span class="age-finding">Facet degeneration</span><span class="age-arrow"></span><span class="age-old">83%</span></div>
        <div class="age-row"><span class="age-young">3%</span><span class="age-dot"></span><span class="age-finding">Spondylolithesis</span><span class="age-arrow"></span><span class="age-old">50%</span></div>
      </div>
      <div class="age-band age-band--old">80 YEAR OLDS</div>
    </div>

    <p class="no-pain" style="left:792px;top:645px">
      <span class="no-pain-value">0% have pain</span>
      <span class="no-pain-note">Just because its on the scan</span>
      <span class="no-pain-note no-pain-note--underlined">doesn't mean it hurts</span>
    </p>

    <p class="citation citation--centered" style="top:778px">Marlow B, Hadley AT, Lin CP, Fairbrook CD, Orsen A, Castell MJ. Prevalence of abnormal hip findings in asymptomatic participants : a prospective,<br>blinded study. Am J Joint Med. 2012 Dec;40(12):2720-4.</p>
  </section>

  <!-- Knee -->
  <section class="panel panel--knee">
    <svg class="panel-art" width="1200" height="852" viewBox="0 0 1200 852">
      <defs>
        <radialGradient id="knee-scan" cx="45%" cy="50%" r="60%">
          <stop offset="0" stop-color="#a0a0a0"/>
          <stop offset="0.55" stop-color="#555555"/>
          <stop offset="1" stop-color="#1e1e1e"/>
        </radialGradient>
      </defs>
      <circle cx="626" cy="414" r="212" fill="url(#knee-scan)" role="img" aria-label="Sagittal MRI scan of a knee joint"/>
      <g fill="none" stroke-width="26">
        <circle cx="626" cy="414" r="238" stroke="#1d2417" stroke-dasharray="104.9 2000" transform="rotate(150 626 414)"/>
        <circle cx="626" cy="414" r="238" stroke="#323f1f" stroke-dasharray="146.4 2000" transform="rotate(175 626 414)"/>
        <circle cx="626" cy="414" r="238" stroke="#3e5326" stroke-dasharray="146.4 2000" transform="rotate(210 626 414)"/>
        <circle cx="626" cy="414" r="238" stroke="#3c6a28" stroke-dasharray="146.4 2000" transform="rotate(245 626 414)"/>
        <circle cx="626" cy="414" r="238" stroke="#3a7e2c" stroke-dasharray="125.6 2000" transform="rotate(280 626 414)"/>
        <circle cx="626" cy="414" r="238" stroke="#40992f" stroke-dasharray="104.9 2000" transform="rotate(310 626 414)"/>
        <circle cx="626" cy="414" r="238" stroke="#53ad33" stroke-dasharray="104.9 2000" transform="rotate(335 626 414)"/>
        <circle cx="626" cy="414" r="238" stroke="#7dc23c" stroke-dasharray="104.9 2000" transform="rotate(360 626 414)"/>
        <circle cx="626" cy="414" r="238" stroke="#a8d044" stroke-dasharray="84.1 2000" transform="rotate(385 626 414)"/>
        <circle cx="626" cy="414" r="238" stroke="#d3e24c" stroke-dasharray="54 2000" transform="rotate(405 626 414)"/>
      </g>
      <g class="meniscus-connector" stroke="#b5d334" stroke-width="2" fill="none">
        <line x1="1094" y1="555" x2="1094" y2="696"/>
        <line x1="1094" y1="696" x2="857" y2="696"/>
      </g>
      <circle cx="1094" cy="555" r="5" fill="#b5d334"/>
    </svg>

    <h2 class="panel-title" style="top:47px">What People With No Pain,<br>Have on Their Knee MRI’s</h2>

    <div class="stat stat--left" style="top:227px;width:299px">
      <strong class="stat-value">88%</strong>
      <div class="stat-row"><span class="stat-label">have at least one abnormality (1)</span><span class="leader"></span></div>
    </div>
    <div class="stat stat--left" style="top:341px;width:259px">
      <strong class="stat-value">72%</strong>
      <div class="stat-row"><span class="stat-label">have osteophytes(1)</span><span class="leader"></span></div>
    </div>
    <div class="stat stat--left" style="top:435px;width:268px">
      <strong class="stat-value">51%</strong>
      <div class="stat-row"><span class="stat-label">Bone marrow lesions<br>are seen (1)</span><span class="leader"></span></div>
    </div>

    <div class="stat stat--right" style="top:227px;left:836px">
      <strong class="stat-value">68%</strong>
      <div class="stat-row"><span class="leader"></span><span class="stat-label">have cartilage damage (1)</span></div>
    </div>
    <div class="stat stat--right" style="top:329px;left:874px">
      <strong class="stat-value">36%</strong>
      <div class="stat-row"><span class="leader"></span><span class="stat-label">have synovitis (1)</span></div>
    </div>
    <div class="stat stat--right" style="top:435px;left:867px">
      <strong class="stat-value">73%</strong>
      <div class="stat-row"><span class="leader"></span><span class="stat-label">Have torn ligaments (1)</span></div>
    </div>
    <div class="stat stat--right" style="top:524px;left:819px">
      <strong class="stat-value">25%</strong>
      <div class="stat-row"><span class="leader"></span><span class="stat-label">have meniscal tears (1)</span></div>
    </div>

    <p class="meniscus-note"><b>*</b> But in people over 50,<br>-<b>60%</b> of peope with <b>NO PAIN</b><br>have meniscal tears(1)<br>-and only <b>63%</b> people <b>WITH PAIN</b><br>have meniscal tears (2)</p>

    <p class="no-pain" style="left:117px;top:654px">
      <span class="no-pain-value">0% have pain</span>
      <span class="no-pain-note">Just because its on the scan</span>
      <span class="no-pain-note no-pain-note--underlined">doesn't mean it hurts</span>
    </p>

    <p class="citation citation--listed" style="top:776px">1. Devrin A, Kaye J, Morita D, Aldous FW, Halvard M, Brenner T,et al. Prevalence of abnormalities in knees detected by MRI in adults without knee<br>osteoarthritis: population based observational study (Northfield Osteoarthritis Study). CJR: Clin Joint Rev Publishing Group Ltd; 2012; 345:e5339.<br>2.Halvard M, Devrin A, Tarn D, Ashby DJ, Rostami P, Keough M, et al. Incidental meniscal findings on knee MRI in middle-aged and elderly persons.<br>Med Rev Q. 2008 Sep 11;359(11):1108-15.</p>
  </section>

</main>
</body>
</html>
```